Business card design needed

Design:
Want the logo/design to have an enviromental feel
Simple look not to busy

Company Info:
Pre purchase building and pest inspections
Registered building practitoner DB-U 48157 (please include building commission logo in design)

Industry/Entity Type

Building

Contact Information for Business Card

Company name:
Fernway Building and Pest inspections

Inspectors:
Dean Parkes 0471 958 214
Jack Severn 0419 562 847
Email: fernbpi@mailbox-demo.net

```html
<!DOCTYPE html>
<html lang="en">
<head>
<meta charset="utf-8">
<title>Fernway Building and Pest inspections – Business Card</title>
<link href="https://fonts.googleapis.com/css2?family=Fjalla+One&family=Overpass:wght@400&display=swap" rel="stylesheet">
<style>
  :root {
    --page-bg: #e6e6e6;
    --card-bg: #ffffff;
    --brand-green: #8dc04a;
    --ink: #1a1a1a;
    --badge-ink: #2a2a40;
    --badge-fill: #e4e4ec;
  }
  * { margin: 0; padding: 0; box-sizing: border-box; }
  html, body {
    width: 1200px; height: 1000px; overflow: hidden;
    background: var(--page-bg);
  }
  .card {
    position: absolute; left: 156px; top: 244px;
    width: 888px; height: 512px;
    background: var(--card-bg);
  }
  .card-frame {
    position: absolute; left: 45px; top: 40px;
    width: 796px; height: 438px;
    border: 1px solid var(--brand-green);
    border-radius: 50px;
  }
  .registration {
    position: absolute; right: 72px; top: 60px;
    text-align: right;
  }
  .registration-badge {
    display: block; width: 168px; height: 48px;
    margin-left: auto;
    background: var(--badge-fill);
    border-radius: 24px;
  }
  .registration-number {
    display: block; margin-top: 4px;
    font-family: "Overpass", sans-serif;
    font-size: 11px; letter-spacing: 2.4px;
    color: var(--badge-ink);
  }
  .brand {
    position: absolute; left: 66px; top: 300px;
    display: flex; align-items: center; gap: 24px;
  }
  .brand-mark {
    width: 112px; height: 112px;
    background: var(--brand-green);
    border-radius: 4px;
    flex: none;
  }
  .brand-name {
    font-family: "Fjalla One", sans-serif;
    font-size: 35px; line-height: 50px;
    color: var(--brand-green);
  }
  .contacts {
    position: absolute; left: 578px; top: 246px;
    font-family: "Overpass", sans-serif;
    color: var(--ink);
  }
  .inspector-name { font-size: 23px; line-height: 30px; }
  .contact-line {
    display: flex; align-items: center; gap: 14px;
    font-size: 24px; line-height: 34px;
    margin-bottom: 10px;
  }
  .contact-line.email { margin-top: 22px; }
  .contact-icon { width: 26px; height: 26px; flex: none; }
</style>
</head>
<body>
  <div class="card">
    <div class="card-frame"></div>

    <div class="registration">
      <span class="registration-badge" role="img" aria-label="Registered building practitioner certification badge"></span>
      <span class="registration-number">DB-U 48157</span>
    </div>

    <div class="brand">
      <div class="brand-mark"></div>
      <div class="brand-name">Fernway Building<br>and<br>Pest inspections</div>
    </div>

    <div class="contacts">
      <div class="inspector-name">Dean Parkes</div>
      <div class="contact-line">
        <svg class="contact-icon" viewBox="0 0 26 26" aria-hidden="true">
          <rect width="26" height="26" rx="5" fill="#8dc04a"/>
          <path d="M8.5 5.5c1.2-.6 2 .2 2.6 1.6l.8 2c.3.9 0 1.5-.8 2l-.9.6c.7 1.9 1.9 3.3 3.4 4.3l.9-.7c.7-.6 1.4-.6 2.1-.1l1.8 1.3c1 .8 1.2 1.7.3 2.6-1.3 1.4-3 1.6-4.6.8-3.5-1.8-6-5-7-8.9-.5-2 .1-4.4 1.4-5.5z" fill="#fff"/>
        </svg>
        <span>0471 958 214</span>
      </div>
      <div class="inspector-name">Jack Severn</div>
      <div class="contact-line">
        <svg class="contact-icon" viewBox="0 0 26 26" aria-hidden="true">
          <rect width="26" height="26" rx="5" fill="#8dc04a"/>
          <path d="M8.5 5.5c1.2-.6 2 .2 2.6 1.6l.8 2c.3.9 0 1.5-.8 2l-.9.6c.7 1.9 1.9 3.3 3.4 4.3l.9-.7c.7-.6 1.4-.6 2.1-.1l1.8 1.3c1 .8 1.2 1.7.3 2.6-1.3 1.4-3 1.6-4.6.8-3.5-1.8-6-5-7-8.9-.5-2 .1-4.4 1.4-5.5z" fill="#fff"/>
        </svg>
        <span>0419 562 847</span>
      </div>
      <div class="contact-line email">
        <svg class="contact-icon" viewBox="0 0 26 26" aria-hidden="true">
          <rect width="26" height="26" rx="5" fill="#8dc04a"/>
          <rect x="5" y="7.5" width="16" height="11" rx="1.5" fill="#fff"/>
          <path d="M5.5 8.5l7.5 5.5 7.5-5.5" fill="none" stroke="#8dc04a" stroke-width="1.4"/>
        </svg>
        <span>fernbpi@mailbox-demo.net</span>
      </div>
    </div>
  </div>
</body>
</html>
```